Brixley Travel letterhead design

We need a design for a simple document where we can dump our own information within it. A simple letterhead style. No address or phone details etc are required. More just our logo and free format. Hope this makes sense !

```html
<!DOCTYPE html>
<html lang="en">
<head>
<meta charset="utf-8">
<title>Brixley Travel Letterhead</title>
<link href="https://fonts.googleapis.com/css2?family=Archivo+Black&family=Archivo:wght@300&display=swap" rel="stylesheet">
<style>
  :root {
    --backdrop: #dbdbdb;
    --paper: #ffffff;
    --brand-navy: #21457a;
    --brand-white: #ffffff;
    --watermark-tint: #e8eaef;
  }
  * { margin: 0; padding: 0; box-sizing: border-box; }
  html, body {
    width: 1200px;
    height: 947px;
    overflow: hidden;
    background: var(--backdrop);
  }
  .letterhead {
    position: absolute;
    left: 364px;
    top: 179px;
    width: 472px;
    height: 606px;
    background: var(--paper);
    overflow: hidden;
  }
  .letterhead__header {
    position: absolute;
    left: 0; top: 0;
    width: 100%;
    height: 53px;
    background: var(--brand-navy);
    display: flex;
    flex-direction: column;
    align-items: center;
    justify-content: center;
    padding-top: 4px;
  }
  .brand-name {
    font-family: "Archivo Black", "Arial Black", sans-serif;
    font-size: 21px;
    line-height: 1;
    color: var(--brand-white);
    letter-spacing: -0.3px;
  }
  .brand-tagline {
    font-family: "Archivo", Arial, sans-serif;
    font-weight: 300;
    font-size: 7.6px;
    line-height: 1;
    margin-top: 2px;
    color: var(--brand-white);
    letter-spacing: 0.1px;
  }
  .letterhead__watermark {
    position: absolute;
    left: 0; top: 0;
    width: 472px;
    height: 606px;
  }
  .watermark-text {
    font-family: "Archivo Black", "Arial Black", sans-serif;
    font-size: 96px;
    fill: var(--watermark-tint);
  }
  .letterhead__footer {
    position: absolute;
    left: 0; bottom: 0;
    width: 100%;
    height: 9px;
    background: var(--brand-navy);
  }
</style>
</head>
<body>
  <div class="letterhead">
    <header class="letterhead__header">
      <span class="brand-name">Brixley</span>
      <span class="brand-tagline">TRAVEL CORPORATION</span>
    </header>

    <svg class="letterhead__watermark" viewBox="0 0 472 606" aria-hidden="true">
      <text class="watermark-text" x="227" y="346" text-anchor="middle"
            textLength="450" lengthAdjust="spacingAndGlyphs"
            transform="rotate(-43.4 227 346)">Brixley</text>
    </svg>

    <footer class="letterhead__footer"></footer>
  </div>
</body>
</html>
```